Christmas Marketing Campaign Graphic Design

We are an online enrichment platform for children aged 3 to 8 years old. We provide real-time online classes in an interactive small-class setting for 4 to 6 students by qualified teachers.

We are going to launch a Christmas marketing campaign for our parents who access our own mobile app and corporate website. We have decided to focus on 1 design in 2 sizes for webpage and 3 sizes for mobile app. Please have a look at our sample design and here are the following details:

1) A "Pop-up Splash". This graphic shows up in our webpage (in 420px x 560px on laptop/tablet and 324px x 432px on mobile) and our mobile app (16:9 on loading page and 375px x 812px on home page,). This graphic design should have a happy Christmas theme, look attractive to parents and entice them to click. It should also include a child (age 3 to 8) in front of a laptop (with or without a parent). It should have two actions for parents: 1) X button on the upper right if the parent wants to cancel; 2) a "View" button to direct the parent to "Sign up for a free trial".

2) "Top Banner". This graphic stays on top of the mobile page (375px x 150px) (after a parent user logs in, the banner shows on top of the home page). The design should be similar to the "Pop-up Splash" just in a different size. If the parent clicks on it, he or she will be directed to "Find out more".

Please refer to our website www.kivamel.com, and find our KIVAMEL mobile app in Orchid Depot and Zentra Fun Depot, and make sure your design style is consistent with our overall branding/design style.
Updates

Dear designers, We have updated our brief with a sample design and clarified that it is essentially 1 design for 4 settings. Please have a look at our updated brief and we look forward to your designs. Thank you!

Target Market(s)

Parents with children aged 3 to 7

Industry/Entity Type

Education

Requirements
Must have
• A child happily attending an online class in front of computer, Christmas theme

```html
<!DOCTYPE html>
<html lang="en">
<head>
<meta charset="utf-8">
<title>Kivamel Christmas Pop-up Splash</title>
<link href="https://fonts.googleapis.com/css2?family=Poppins:ital,wght@0,500;0,600;0,700;1,500&display=swap" rel="stylesheet">
<style>
  :root {
    --peach: #f3d8c3;
    --peach-light: #f8e6d8;
    --cream: #fcf1e8;
    --navy: #1f3f8f;
    --red: #e8423b;
    --close-red: #e63b3b;
    --magenta: #d0347a;
    --brand-green: #5fae3c;
    --girl-tone: #c9b7c4;
    --snow: #ffffff;
    --ornament: #d9333a;
    --ornament-dark: #263a5c;
    --leaf: #d04a4a;
    --white: #ffffff;
  }
  html, body {
    margin: 0;
    padding: 0;
    width: 900px;
    height: 1200px;
    overflow: hidden;
    background: var(--peach);
  }
  .splash {
    position: relative;
    width: 900px;
    height: 1200px;
    overflow: hidden;
    background: linear-gradient(180deg, var(--peach-light) 0%, var(--peach) 45%);
    font-family: "Poppins", sans-serif;
    color: var(--navy);
  }
  .brand {
    position: absolute;
    left: 26px;
    top: 14px;
  }
  .brand-name {
    display: block;
    font-weight: 700;
    font-size: 46px;
    line-height: 1;
    letter-spacing: 1px;
    color: var(--brand-green);
  }
  .brand-url {
    display: block;
    margin-top: 8px;
    font-weight: 500;
    font-size: 21px;
    letter-spacing: 1.5px;
    color: var(--magenta);
  }
  .tagline {
    position: absolute;
    right: 64px;
    top: 6px;
    margin: 0;
    width: 440px;
    text-align: right;
    font-style: italic;
    font-weight: 500;
    font-size: 22px;
    line-height: 1.25;
    color: var(--navy);
  }
  .close-button {
    position: absolute;
    right: 0;
    top: 0;
    width: 48px;
    height: 48px;
    background: var(--close-red);
    display: flex;
    align-items: center;
    justify-content: center;
  }
  .leaf-decoration {
    position: absolute;
    right: 0;
    top: 64px;
    width: 70px;
    height: 110px;
    border-radius: 60px 0 0 60px;
    background: linear-gradient(200deg, var(--leaf), rgba(208,74,74,0));
    opacity: 0.7;
  }
  .headline {
    position: absolute;
    left: 0;
    right: 0;
    top: 128px;
    margin: 0;
    text-align: center;
    font-weight: 600;
    color: var(--navy);
    line-height: 1.12;
  }
  .headline-top { display: block; font-size: 58px; }
  .headline-bottom { display: block; font-size: 64px; font-weight: 700; }
  .subjects {
    position: absolute;
    left: 0; right: 0;
    top: 284px;
    margin: 0;
    text-align: center;
    font-weight: 600;
    font-size: 30px;
    color: var(--red);
  }
  .subjects .divider { color: var(--navy); font-weight: 500; }
  .subjects .subject-list { font-weight: 500; }
  .offer {
    position: absolute;
    left: 0; right: 0;
    top: 350px;
    margin: 0;
    text-align: center;
    font-weight: 600;
    font-size: 39px;
    line-height: 1.28;
    color: var(--navy);
  }
  .plus {
    position: absolute;
    left: 0; right: 0;
    top: 452px;
    margin: 0;
    text-align: center;
    font-weight: 600;
    font-size: 42px;
    color: var(--navy);
  }
  .prize {
    position: absolute;
    left: 0; right: 0;
    top: 500px;
    margin: 0;
    text-align: center;
    font-weight: 600;
    font-size: 36px;
    color: var(--red);
  }
  .view-button {
    position: absolute;
    left: 347px;
    top: 597px;
    width: 206px;
    height: 72px;
    border-radius: 36px;
    background: var(--navy);
    color: var(--white);
    font-weight: 700;
    font-size: 36px;
    letter-spacing: 1px;
    display: flex;
    align-items: center;
    justify-content: center;
    text-decoration: none;
  }
  .ornament {
    position: absolute;
    border-radius: 50%;
  }
  .ornament-red { background: var(--ornament); }
  .ornament-dark { background: var(--ornament-dark); }
  .snow-ground {
    position: absolute;
    left: 0;
    top: 640px;
    width: 900px;
    height: 560px;
  }
  .child-scene {
    position: absolute;
    left: 0;
    top: 760px;
    width: 590px;
    height: 440px;
    border-radius: 0 200px 0 0;
    background: linear-gradient(160deg, #d8c6cf 0%, var(--girl-tone) 55%, #b9c2cc 100%);
  }
  .snowman {
    position: absolute;
    left: 600px;
    top: 730px;
    width: 250px;
    height: 470px;
    border-radius: 125px 125px 20px 20px;
    background: linear-gradient(180deg, #f4f4f6 0%, var(--snow) 60%, #f1eef0 100%);
  }
  .ages {
    position: absolute;
    left: 640px;
    top: 1003px;
    width: 170px;
    margin: 0;
    text-align: center;
    font-weight: 500;
    font-size: 27px;
    line-height: 1.25;
    color: var(--navy);
  }
  .gifts {
    position: absolute;
    left: 490px;
    top: 1110px;
    width: 100px;
    height: 90px;
    border-radius: 6px;
    background: linear-gradient(180deg, #4a8fd0, #2f6eb5);
  }
  .berries {
    position: absolute;
    left: 830px;
    top: 1080px;
    width: 70px;
    height: 120px;
    border-radius: 35px 0 0 0;
    background: linear-gradient(180deg, var(--leaf), #3d4f7a);
    opacity: 0.8;
  }
</style>
</head>
<body>
<main class="splash">
  <div class="brand">
    <span class="brand-name">KIVAMEL</span>
    <span class="brand-url">www.kivamel.com</span>
  </div>

  <p class="tagline">#1 Multi-Subject Online Enrichment Platform for Young Learners</p>

  <a class="close-button" href="#" aria-label="Close">
    <svg width="26" height="26" viewBox="0 0 26 26" aria-hidden="true">
      <path d="M3 3 L23 23 M23 3 L3 23" stroke="#ffffff" stroke-width="3.5" stroke-linecap="round"/>
    </svg>
  </a>

  <div class="leaf-decoration" role="img" aria-label="Red winter leaves and berries"></div>

  <h1 class="headline">
    <span class="headline-top">PREPARE YOUR CHILD</span>
    <span class="headline-bottom">FOR 2022!</span>
  </h1>

  <p class="subjects">LIVE ONLINE CLASSES <span class="divider">|</span> <span class="subject-list">ENGLISH, CHINESE, MATHS</span></p>

  <p class="offer">Enjoy up to 28 FREE Classes<br>(worth $420)</p>
  <p class="plus">+</p>
  <p class="prize">Stand a chance to win a laptop worth $500!</p>

  <div class="ornament ornament-dark" style="left:72px;top:352px;width:40px;height:40px;" role="img" aria-label="Christmas bauble"></div>
  <div class="ornament ornament-red" style="left:48px;top:412px;width:50px;height:50px;" role="img" aria-label="Christmas bauble"></div>
  <div class="ornament ornament-dark" style="left:668px;top:566px;width:34px;height:34px;" role="img" aria-label="Christmas bauble"></div>
  <div class="ornament ornament-red" style="left:758px;top:672px;width:48px;height:48px;" role="img" aria-label="Christmas bauble"></div>

  <svg class="snow-ground" viewBox="0 0 900 560" aria-hidden="true">
    <path d="M0 110 C 160 60, 300 70, 450 90 C 620 112, 760 40, 900 60 L900 560 L0 560 Z" fill="#f9ebe0"/>
    <path d="M0 220 C 200 160, 380 190, 520 210 C 680 232, 800 180, 900 190 L900 560 L0 560 Z" fill="#fcf3ec"/>
  </svg>

  <a class="view-button" href="#">VIEW</a>

  <div class="child-scene" role="img" aria-label="Young girl with blue headphones smiling at a laptop during an online class"></div>
  <div class="snowman" role="img" aria-label="Snowman with red scarf and hat"></div>
  <p class="ages">FOR AGES<br>3 - 7</p>
  <div class="gifts" role="img" aria-label="Blue wrapped gift boxes"></div>
  <div class="berries" role="img" aria-label="Red berry branch"></div>
</main>
</body>
</html>
```